Tolvani Crafts

I would like to have a more comprehensive e-commerce website.

Please use my current website as reference and its content: https://tolvanicrafts.com/.

Please code the website. I'd like to have e-commerce functionalities.

```html
<!DOCTYPE html>
<html lang="en">
<head>
<meta charset="utf-8">
<title>Tolvani Crafts</title>
<link href="https://fonts.googleapis.com/css2?family=Londrina+Solid:wght@400;900&family=Poppins:ital,wght@0,400;0,500;0,600;0,700;1,400&display=swap" rel="stylesheet">
<style>
:root{
  --red:#f4454f;
  --navy:#0e2f3e;
  --footer:#163f52;
  --ink:#222;
  --muted:#555;
  --display:"Londrina Solid", sans-serif;
  --body:"Poppins", sans-serif;
}
*{box-sizing:border-box;margin:0;padding:0}
html,body{width:1200px;height:4781px;overflow:hidden;background:#fff;font-family:var(--body);color:var(--ink)}
.page{position:relative;width:1200px;height:4781px}
.abs{position:absolute}
.display{font-family:var(--display);font-weight:900;text-transform:uppercase;color:var(--navy);letter-spacing:.5px}
.center{text-align:center;left:0;width:1200px}

/* header */
.topbar{top:0;left:0;width:1200px;height:5px;background:var(--navy)}
.header{top:5px;left:0;width:1200px;height:105px;background:#fff}
.nav{top:48px;left:110px;display:flex;gap:32px;font-family:var(--display);font-weight:900;font-size:15px;text-transform:uppercase;color:var(--navy)}
.nav .active{color:var(--red)}
.brand-tab{top:60px;left:470px;width:260px;height:80px;background:#fff;border-radius:0 0 40px 40px;z-index:3}
.brand{top:18px;left:0;width:1200px;display:flex;flex-direction:column;align-items:center;gap:6px;z-index:4}
.brand .dot{width:62px;height:62px;border-radius:50%;background:var(--red)}
.brand .name{font-family:var(--body);font-weight:700;font-size:16px;color:var(--navy);letter-spacing:.5px}
.search{top:48px;left:780px;font-family:var(--display);font-weight:900;font-size:15px;color:var(--navy)}
.icon-search{top:46px;left:928px}
.user{top:40px;left:977px;width:40px;height:40px;border-radius:50%;background:var(--navy);display:flex;align-items:center;justify-content:center}
.cart{top:40px;left:1033px;width:40px;height:40px;border-radius:50%;background:var(--red);display:flex;align-items:center;justify-content:center}

/* hero */
.hero{top:110px;left:0;width:1200px;height:588px;background:linear-gradient(100deg,#f2613f 0%,#f4654a 45%,#f58a70 75%,#d9b9ad 100%)}
.hero-photo{top:110px;left:700px;width:500px;height:588px;background:radial-gradient(ellipse at 55% 50%,#e6e3de 0%,#cfcac3 35%,#7a625b 60%,#6a5853 100%)}
.hero-kicker{top:282px;left:126px;font-family:var(--body);font-weight:600;font-size:29px;color:#fff}
.hero-title{top:326px;left:126px;font-family:var(--display);font-weight:900;font-size:52px;line-height:55px;color:#fff;text-transform:uppercase}
.btn{display:inline-flex;align-items:center;justify-content:center;border-radius:30px;font-family:var(--display);font-weight:900;color:#fff}
.hero-btn{top:467px;left:127px;width:148px;height:54px;background:var(--navy);font-size:19px}
.dots{top:580px;left:130px;display:flex;gap:6px}
.dots span{width:10px;height:10px;border-radius:50%;background:#fff}
.dots span:first-child{background:none;border:1.5px solid #fff}

/* favourites */
.section-title{font-size:40px}
.products{top:872px;left:126px;display:flex;gap:16px}
.product{width:225px;text-align:center}
.product .ph{height:241px}
.product .pname{margin-top:22px;font-size:17px;color:#333}
.product .stars{margin-top:4px;color:var(--red);font-size:12px;letter-spacing:1px}
.product .price{margin-top:2px;font-weight:600;font-size:15px}
.progress{top:1274px;left:126px;width:948px;height:2px;background:#ddd}
.progress span{position:absolute;left:0;top:-2px;width:91px;height:5px;background:var(--red)}

/* welcome */
.welcome-mark{top:1340px;left:535px;width:130px;height:150px;display:flex;align-items:center;justify-content:center}
.welcome-mark span{width:110px;height:110px;border-radius:50%;background:var(--red)}
.welcome-title{top:1512px;font-size:44px}
.welcome-text{top:1580px;left:200px;width:800px;text-align:center;font-size:18px;line-height:27px;color:#222}

/* sale grid */
.sale{top:1777px;left:0;width:388px;height:755px;background:var(--red)}
.sale .frame{position:absolute;top:22px;left:17px;right:17px;bottom:22px;border:2px solid rgba(255,255,255,.8)}
.sale-head{top:2030px;left:0;width:388px;text-align:center;color:#fff}
.sale-head .big{font-family:var(--display);font-weight:900;font-size:42px;text-transform:uppercase;line-height:48px}
.sale-head .big small{font-size:24px}
.sale-head .lim{font-family:var(--body);font-weight:400;font-size:24px;text-transform:none}
.sale-text{top:2150px;left:44px;width:300px;text-align:center;color:#fff;font-size:18px;line-height:25px}
.sale-btn{top:2259px;left:124px;width:140px;height:42px;background:#fff;color:var(--red);font-size:17px}
.tile{width:388px;height:369px}
.tile-label{position:absolute;bottom:32px;left:0;width:100%;text-align:center;color:#fff;font-weight:600;font-size:30px;text-shadow:0 1px 4px rgba(0,0,0,.35)}

/* testimonials */
.t-card{top:2782px;left:204px;width:792px;height:307px;background:#fff;box-shadow:0 0 14px rgba(0,0,0,.08)}
.avatar{top:2755px;left:541px;width:118px;height:118px;border-radius:50%;background:radial-gradient(circle at 55% 55%,#f7e18a 0%,#e2c062 30%,#3b3a36 70%);border:3px solid #fff}
.t-name{top:2893px;font-weight:500;font-size:19px;letter-spacing:1px;color:#333}
.t-text{top:2928px;left:260px;width:680px;text-align:center;font-style:italic;font-size:16px;line-height:22px;color:#555}
.t-stars{top:3030px;color:var(--red);font-size:30px;letter-spacing:2px}
.arrow-l{top:2926px;left:143px}
.arrow-r{top:2926px;left:1031px}

/* made with love */
.love{top:3218px;left:0;width:1200px;height:496px;background:linear-gradient(90deg,#c9d0c9 0%,#dfe3e1 35%,#eceded 55%,#e4e4e4 100%)}
.love-photo{top:3218px;left:620px;width:580px;height:496px;background:radial-gradient(ellipse at 55% 60%,#f4f4f4 0%,#d5d5d5 35%,#c3c3c3 55%,#ececec 80%)}
.love-title{top:3352px;left:160px;font-family:var(--display);font-weight:900;font-size:62px;color:var(--navy)}
.love-text{top:3434px;left:158px;width:420px;font-size:20px;line-height:29px;color:#333}
.love-btn{top:3512px;left:160px;width:138px;height:42px;background:var(--red);font-size:17px}

/* instagram */
.insta{top:3923px;left:108px;display:flex;gap:17px}
.insta div{width:233px;height:304px}

/* footer */
.footer{top:4344px;left:0;width:1200px;height:437px;background:var(--footer)}
.f-brand{top:4440px;left:140px;width:200px;display:flex;flex-direction:column;align-items:center;gap:10px}
.f-brand .dot{width:64px;height:64px;border-radius:50%;background:var(--red)}
.f-brand .name{font-weight:700;font-size:16px;color:#fff}
.social{top:4580px;left:196px;display:flex;gap:4px}
.social span{width:40px;height:40px;border-radius:50%;border:2px solid var(--red)}
.f-col h4{font-weight:600;font-size:17px;color:var(--red);text-transform:uppercase;margin-bottom:16px}
.f-col li{list-style:none;color:#fff;font-size:14px;line-height:29.5px}
.f-news p{color:#fff;font-size:14px;line-height:20px;width:330px}
.f-input{top:4550px;left:785px;width:189px;height:47px;background:#fff;font-size:13px;color:#555;padding:15px 16px}
.f-sub{top:4550px;left:974px;width:137px;height:47px;background:var(--red);color:#fff;font-weight:600;font-size:14px;display:flex;align-items:center;justify-content:center}
.copy{top:4713px;color:#fff;font-size:17px}
</style>
</head>
<body>
<div class="page">

  <!-- header -->
  <div class="abs topbar"></div>
  <header class="abs header"></header>
  <nav class="abs nav"><span class="active">Home</span><span>About Us</span><span>Products</span><span>Contact Us</span></nav>
  <div class="abs brand-tab"></div>
  <div class="abs brand"><span class="dot"></span><span class="name">TOLVANI CRAFTS</span></div>
  <div class="abs search">SEARCH</div>
  <svg class="abs icon-search" width="22" height="22" viewBox="0 0 22 22" fill="none" stroke="#0e2f3e" stroke-width="2"><circle cx="9" cy="9" r="6.5"/><path d="M14 14l5 5"/></svg>
  <div class="abs user"><svg width="18" height="18" viewBox="0 0 18 18" fill="none" stroke="#fff" stroke-width="1.8"><circle cx="9" cy="6" r="3.3"/><path d="M3 16c0-3.3 2.7-5 6-5s6 1.7 6 5"/></svg></div>
  <div class="abs cart"><svg width="18" height="18" viewBox="0 0 18 18" fill="none" stroke="#fff" stroke-width="1.8"><rect x="3" y="6" width="12" height="10" rx="1.5"/><path d="M6 6V5a3 3 0 0 1 6 0v1"/></svg></div>

  <!-- hero -->
  <section class="abs hero" role="img" aria-label="Warm red watercolour backdrop with faint roses"></section>
  <div class="abs hero-photo" role="img" aria-label="Concrete bowl candle with succulents and a thank-you card on a stone ledge"></div>
  <div class="abs hero-kicker">Tolvani Crafts!</div>
  <h1 class="abs hero-title">Handcrafted Candles<br>Inspired by the Southwest</h1>
  <a class="abs btn hero-btn">Shop Now</a>
  <div class="abs dots"><span></span><span></span><span></span><span></span><span></span></div>

  <!-- favourites -->
  <h2 class="abs center display section-title" style="top:778px">A Few of Our Favourite Things</h2>
  <div class="abs products">
    <div class="product"><div class="ph" role="img" aria-label="Textured concrete candles with handmade tags" style="background:linear-gradient(160deg,#e9e9e9,#b9b9b6)"></div><div class="pname">Product Name</div><div class="stars">★★★★★</div><div class="price">$7.00</div></div>
    <div class="product"><div class="ph" role="img" aria-label="Round concrete candle with white wax" style="background:linear-gradient(160deg,#f2f2f2,#c9c9c6)"></div><div class="pname">Product Name</div><div class="stars">★★★★★</div><div class="price">$7.00</div></div>
    <div class="product"><div class="ph" role="img" aria-label="Lidded candle jar with succulent decoration on wood" style="background:linear-gradient(90deg,#5a3a2a 0%,#6b4a36 40%,#b5aca4 100%)"></div><div class="pname">Product Name</div><div class="stars">★★★★★</div><div class="price">$7.00</div></div>
    <div class="product"><div class="ph" role="img" aria-label="Concrete candles among desert stones" style="background:linear-gradient(170deg,#8d7e6b,#a79f93 50%,#6e6a62)"></div><div class="pname">Product Name</div><div class="stars">★★★★★</div><div class="price">$7.00</div></div>
  </div>
  <div class="abs progress"><span></span></div>

  <!-- welcome -->
  <div class="abs welcome-mark"><span></span></div>
  <h2 class="abs center display welcome-title">Welcome to Tolvani Crafts!</h2>
  <p class="abs welcome-text">We are a family-owned business passionate about creating beautiful, eco-friendly candles that capture the essence of the Southwest. Our candles are handcrafted by Mexican-American women who pour their love and creativity into each piece.</p>

  <!-- sale grid -->
  <div class="abs sale"><div class="frame"></div></div>
  <div class="abs sale-head"><div class="big"><small>Sale</small> Up to 80%</div><div class="big">Off <span class="lim">Limited offer</span></div></div>
  <p class="abs sale-text">Tolvani Crafts offers<br>a variety of candles to suit<br>your taste and style.</p>
  <a class="abs btn sale-btn">Shop Now</a>

  <div class="abs tile" style="top:1777px;left:406px;background:radial-gradient(circle at 50% 45%,#efefef 0%,#cfcfcf 40%,#8b7c6c 75%)" role="img" aria-label="Dimpled concrete candle on river rocks"><span class="tile-label">Sola</span></div>
  <div class="abs tile" style="top:1777px;left:812px;background:linear-gradient(180deg,#9aa09a 0%,#c7c9c6 45%,#b8bcba 80%,#8c9fa8 100%)" role="img" aria-label="Concrete planter with green succulent"><span class="tile-label">Mesa</span></div>
  <div class="abs tile" style="top:2163px;left:406px;background:linear-gradient(90deg,#9c9a95 0%,#d8d6d2 45%,#4a3024 100%)" role="img" aria-label="Lidded candle with succulent topper tied with twine"><span class="tile-label">Vero</span></div>
  <div class="abs tile" style="top:2163px;left:812px;background:radial-gradient(circle at 50% 40%,#e9b9a5 0%,#c9d3d9 45%,#aebbc3 100%)" role="img" aria-label="Glass bowl candle topped with colourful wax donuts"><span class="tile-label">New Candles</span></div>

  <!-- testimonials -->
  <h2 class="abs center display section-title" style="top:2666px">Client Testimonials</h2>
  <div class="abs t-card"></div>
  <div class="abs avatar" role="img" aria-label="Lit round candle"></div>
  <div class="abs center t-name">MARISOL K</div>
  <p class="abs t-text">Lorem ipsum dolor sit ameconsectetur adipiscing elitse do eiusmod tempor idnt ut labore et dolore mag na aliquaLorem ipsum dolor sit ameconsectetur adipiscing elitse do eiusmod tempor incid idnt ut labore et dolore mag na aliqua. Quis ipsum suspen disse ultrices gravida. is ipsum suspen ds gravida.</p>
  <div class="abs center t-stars">★★★★★</div>
  <svg class="abs arrow-l" width="16" height="24" viewBox="0 0 16 24" fill="none" stroke="#888" stroke-width="2"><path d="M11 4L4 12l7 8"/></svg>
  <svg class="abs arrow-r" width="16" height="24" viewBox="0 0 16 24" fill="none" stroke="#888" stroke-width="2"><path d="M5 4l7 8-7 8"/></svg>

  <!-- made with love -->
  <section class="abs love" role="img" aria-label="Soft faded greenery backdrop"></section>
  <div class="abs love-photo" role="img" aria-label="Three dimpled concrete tealight candles"></div>
  <h2 class="abs love-title">Made with love</h2>
  <p class="abs love-text">Lorem ipsum dolor sit amet, consectetur adipiscing elit, sed do eiusmod tem.</p>
  <a class="abs btn love-btn">Shop Now</a>

  <!-- instagram -->
  <h2 class="abs center display section-title" style="top:3820px">Folow Us Instagram</h2>
  <div class="abs insta">
    <div role="img" aria-label="Lit candle bowl with succulent from above" style="background:radial-gradient(circle,#e9c9a6 0%,#c08a5c 45%,#2a2420 80%)"></div>
    <div role="img" aria-label="Candles with purple and blue wax succulents" style="background:linear-gradient(150deg,#9a8fb8,#dcdad6 55%,#a08a6a)"></div>
    <div role="img" aria-label="Dimpled concrete tealights on white" style="background:radial-gradient(circle at 50% 60%,#f3f3f3,#cfcfcf 50%,#eaeaea)"></div>
    <div role="img" aria-label="White planter with succulents outdoors" style="background:linear-gradient(180deg,#4d6a3e,#8f9a7c 50%,#6f5d52)"></div>
  </div>

  <!-- footer -->
  <footer class="abs footer"></footer>
  <div class="abs f-brand"><span class="dot"></span><span class="name">TOLVANI CRAFTS</span></div>
  <div class="abs social"><span></span><span></span></div>
  <div class="abs f-col" style="top:4443px;left:425px"><h4>Customer</h4><ul><li>Shop</li><li>FAQs</li><li>Contact Us</li><li>Reviews</li></ul></div>
  <div class="abs f-col" style="top:4443px;left:597px"><h4>Products</h4><ul><li>Sola Collection</li><li>Mesa Collection</li><li>New Collection</li><li>Vero Collection</li></ul></div>
  <div class="abs f-col f-news" style="top:4443px;left:785px"><h4>Newsletter</h4><p>Receive access to VIP discounts, new product launches and more.</p></div>
  <div class="abs f-input">Email:</div>
  <div class="abs f-sub">SUBSCRIBE</div>
  <div class="abs center copy">© 2025 Tolvani Crafts. All rights are reserved.</div>

</div>
</body>
</html>
```